Package of web graphics needed

Utilizing a recently selected logo from a Pixel Harbor contest, we need to have some ads, fb cover, home page slide image created for our new 844-Toll-Free Number Product. Please feel free to check our site at www.ringvantagehub.com

You'll find attached the 844 toll free logo in 2 layouts.

Here are the ads and dimensions of each that are needed:
1.)Banners/ads - 468x60
468×60 px
125×125 px
120×600 px
120x90 px
88×31 px button
5.)FB Cover - 851 x 315
6.)Home page slider image - 944 x 328

Here is the text & some ideas to use for these. Feel free to use different versions depending on which ad they work better on:
-

Market Your Business in a Memorable Way – Pre-Order Yours Today, Deadline: Dec. 7th
[include logo]
-
[844 logo] Don't Miss out on your chance to finally get a great vanity!

Order Yours Today
-

Don't Miss out on your chance to finally get a great vanity!
Dec. 7th Deadline to pre-order

Don't Ignore 844!– The newest toll free prefix – Coming Dec. 7th – Get Yours Today

FB COVER guidelines -
Requirements:
Include the logo
Limited Time Left – Get your Reservation in by December 7th

HOME PAGE Image Slide:
Use the logo,

Couple of Ideas we're interested in seeing:

[Billboard sign stock image … with the number 877-Grab-ONE on the billboard]
[844 logo and caricature] [1 caricature looking surprised]

```html
<!DOCTYPE html>
<html lang="en">
<head>
<meta charset="utf-8">
<title>Ringvantage – 844 Web Ad Package</title>
<link rel="stylesheet" href="https://fonts.googleapis.com/css2?family=Roboto:wght@400;500;700&display=swap">
<style>
  :root {
    --board: #1d1d1d;
    --navy: #0d2b52;
    --navy-deep: #0a2244;
    --green: #5cb531;
    --yellow: #f7e11a;
    --button-yellow: #f5d21c;
    --white: #ffffff;
    --ink: #1a2a44;
    --panel-dark: rgba(60, 60, 60, 0.88);
    --sky-top: #5d9ad6;
    --sky-mid: #bcd6ef;
    --grey-mid: #8d9aa5;
  }
  * { box-sizing: border-box; margin: 0; padding: 0; }
  html, body { width: 1200px; height: 770px; overflow: hidden; }
  body {
    background: var(--board);
    font-family: "Roboto", Arial, sans-serif;
    position: relative;
  }
  .ad { position: absolute; overflow: hidden; }
  .brand {
    font-family: "Roboto", Arial, sans-serif;
    font-weight: 700;
    color: var(--navy);
    display: flex; align-items: center; gap: 5px;
    white-space: nowrap;
  }
  .brand-square { background: var(--green); display: inline-block; }
  .photo { position: absolute; }

  /* Facebook cover */
  .fb-cover { left: 138px; top: 138px; width: 683px; height: 237px; }
  .fb-cover .photo {
    inset: 0;
    background: linear-gradient(180deg, var(--sky-top) 0%, var(--sky-mid) 45%, #e9eef2 68%, #f4f6f8 100%);
  }
  .fb-cover .banner-row {
    position: absolute; left: 98px; top: 165px; right: 40px;
    display: flex; align-items: center; gap: 40px;
  }
  .fb-cover .brand { font-size: 30px; }
  .fb-cover .brand-square { width: 24px; height: 24px; }
  .fb-cover .headline {
    font-size: 15.5px; font-weight: 500; color: var(--navy); text-align: center; line-height: 1.1;
  }
  .fb-cover .fine {
    font-size: 7.5px; font-weight: 500; color: var(--ink); margin-top: 9px; text-align: center; word-spacing: 2px;
  }

  /* Home page slider */
  .slider { left: 102px; top: 420px; width: 616px; height: 226px; }
  .slider .photo {
    inset: 0;
    background: linear-gradient(180deg, #d4d9cf 0%, #a9b2a4 40%, #6f7570 70%, #d8d8d8 100%);
  }
  .slider .sign {
    position: absolute; top: 36px; width: 94px; height: 154px;
    background: var(--white); border: 4px solid #2a2a2a;
    display: flex; align-items: center; justify-content: center;
  }
  .slider .sign-left { left: 59px; }
  .slider .sign-right { left: 460px; }
  .slider .sign .brand { font-size: 13px; }
  .slider .sign .brand-square { width: 9px; height: 9px; }
  .slider .message {
    position: absolute; left: 161px; top: 39px; width: 296px; height: 153px;
    background: var(--panel-dark); color: var(--white); text-align: center; padding-top: 20px;
  }
  .slider .message h2 { font-size: 25px; font-weight: 500; line-height: 1.05; }
  .slider .message p { font-size: 16px; font-weight: 500; color: var(--green); margin-top: 16px; line-height: 1.05; }

  /* 125 x 125 square */
  .square { left: 866px; top: 199px; width: 90px; height: 90px; background: var(--white); border: 1px solid #3a4d6a; }
  .square .brand-bar { height: 20px; display: flex; align-items: center; justify-content: center; }
  .square .brand { font-size: 9px; gap: 3px; }
  .square .brand-square { width: 6px; height: 6px; }
  .square .body {
    height: 69px;
    background: linear-gradient(180deg, #b1bac3, var(--grey-mid));
    color: var(--white); text-align: center; font-size: 8px; font-weight: 500; line-height: 1.05;
    padding-top: 4px;
  }
  .square .cta {
    margin: 5px 4px 0; background: var(--navy); border-radius: 5px;
    font-size: 6.5px; padding: 3px 2px; line-height: 1.1;
  }

  /* 120 x 90 */
  .small-rect { left: 866px; top: 369px; width: 90px; height: 65px; background: var(--navy); }
  .small-rect .brand-bar { height: 18px; background: var(--white); display: flex; align-items: center; justify-content: center; }
  .small-rect .brand { font-size: 9px; gap: 3px; }
  .small-rect .brand-square { width: 6px; height: 6px; }
  .small-rect .body { color: var(--white); text-align: center; font-size: 7.5px; font-style: italic; line-height: 1.1; padding-top: 2px; }
  .small-rect .body strong { color: var(--yellow); display: block; font-weight: 700; }

  /* 88 x 31 button */
  .button-ad { left: 890px; top: 534px; width: 64px; height: 22px; background: var(--white); display: flex; align-items: center; justify-content: center; }
  .button-ad .brand { font-size: 8px; gap: 2px; }
  .button-ad .brand-square { width: 5px; height: 5px; }

  /* 120 x 600 skyscraper */
  .skyscraper { left: 993px; top: 141px; width: 87px; height: 434px; background: var(--navy); text-align: center; color: var(--white); }
  .skyscraper .kicker { font-size: 13px; font-weight: 700; margin-top: 19px; }
  .skyscraper .prefix { font-size: 32px; font-weight: 700; color: var(--yellow); margin-top: 8px; }
  .skyscraper .lines { font-size: 20px; font-weight: 700; line-height: 1.5; margin-top: 5px; }
  .skyscraper .date { font-size: 9.5px; font-weight: 700; margin-top: 22px; }
  .skyscraper .cta { font-size: 9.5px; font-weight: 700; color: var(--yellow); margin-top: 8px; }
  .skyscraper .photo {
    left: 0; right: 0; bottom: 0; height: 150px;
    background: linear-gradient(180deg, #c7cdd2 0%, #9aa3a8 60%, #5f6568 100%);
  }
  .skyscraper .sign {
    position: absolute; left: 7px; bottom: 28px; width: 66px; height: 107px;
    background: var(--white); border: 3px solid #2a2a2a;
    display: flex; align-items: center; justify-content: center;
  }
  .skyscraper .sign .brand { font-size: 9.5px; gap: 3px; }
  .skyscraper .sign .brand-square { width: 6px; height: 6px; }

  /* 468 x 60 leaderboard */
  .leaderboard {
    left: 744px; top: 604px; width: 337px; height: 43px; background: var(--navy-deep);
    display: flex; align-items: center; padding: 0 4px;
  }
  .leaderboard .brand-box { width: 57px; height: 37px; background: var(--white); display: flex; align-items: center; justify-content: center; }
  .leaderboard .brand { font-size: 9px; gap: 2px; }
  .leaderboard .brand-square { width: 5px; height: 5px; }
  .leaderboard .headline { flex: 1; color: var(--white); font-size: 12px; text-align: center; line-height: 1.1; }
  .leaderboard .cta {
    width: 72px; height: 29px; border-radius: 7px; background: var(--button-yellow);
    border: 1px solid #b79a0c; color: var(--navy); font-size: 9px; font-weight: 500;
    display: flex; align-items: center; justify-content: center; text-align: center; line-height: 1.1;
  }
</style>
</head>
<body>

  <section class="ad fb-cover">
    <div class="photo" role="img" aria-label="Photo of a cheerful group of people with raised arms under a blue sky, holding a white banner"></div>
    <div class="banner-row">
      <div class="brand"><span class="brand-square"></span>Ringvantage</div>
      <div>
        <p class="headline">Don't Miss out on your chance<br>to finally get a great vanity!</p>
        <p class="fine">Limited Time Left &nbsp; Get your Reservation in by December 7th</p>
      </div>
    </div>
  </section>

  <section class="ad slider">
    <div class="photo" role="img" aria-label="Photo of two city bus shelters with advertising light boxes, trees behind"></div>
    <div class="sign sign-left"><div class="brand"><span class="brand-square"></span>Ringvantage</div></div>
    <div class="message">
      <h2>Market Your Business<br>in a Memorable Way</h2>
      <p>Pre-Order Yours Today,<br>Deadline: Dec. 7th</p>
    </div>
    <div class="sign sign-right"><div class="brand"><span class="brand-square"></span>Ringvantage</div></div>
  </section>

  <section class="ad square">
    <div class="brand-bar"><div class="brand"><span class="brand-square"></span>Ringvantage</div></div>
    <div class="body">
      Don't Miss out on<br>your chance to<br>finally get a great<br>vanity!
      <div class="cta">Dec. 7th Deadline<br>to pre-order</div>
    </div>
  </section>

  <section class="ad small-rect">
    <div class="brand-bar"><div class="brand"><span class="brand-square"></span>Ringvantage</div></div>
    <div class="body">Don't Miss out on<br>your chance to finally<br>get a great vanity!<strong>Order Yours Today</strong></div>
  </section>

  <section class="ad button-ad">
    <div class="brand"><span class="brand-square"></span>Ringvantage</div>
  </section>

  <section class="ad skyscraper">
    <p class="kicker">Don't Ignore</p>
    <p class="prefix">844!</p>
    <p class="lines">the<br>newest<br>toll free<br>prefix</p>
    <p class="date">Coming Dec. 7th</p>
    <p class="cta">Get Yours Today</p>
    <div class="photo" role="img" aria-label="Photo of a bus shelter advertising light box"></div>
    <div class="sign"><div class="brand"><span class="brand-square"></span>Ringvantage</div></div>
  </section>

  <section class="ad leaderboard">
    <div class="brand-box"><div class="brand"><span class="brand-square"></span>Ringvantage</div></div>
    <p class="headline">Don't Miss out on your chance<br>to finally get a great vanity!</p>
    <div class="cta">Order Yours<br>Today</div>
  </section>

</body>
</html>
```